International professional tennis coach needs a book cover design

This is my 2nd published book, the first one was a #1 on the best seller. I'm looking for a world class book cover design for this new book. The name of my first book was 5 Baseline Habits to Unlock Your Rally Rhythm, located on Brimlow.com

The title of the new book:

Title: The Craft of Steady Rallies
Subtitle: Building a Tactical Margin by Way of Opponent Insight

I'm uploading our new CRAFT OF STEADY logo that I'd like for you to use as the centerpiece of the book design along with a 21st century design feel that incorporates what the book topic is below::

--> This book is about building competitive intelligence by using tennis data analytics to develop and expand a player's strategic advantage for match play. <--

The colors we would like to use are Blue, Yellow, and Green. These shades of these colors should be bold! (You will see the bold color examples of blues, yellows, and greens that I'm talking about in the logos that are attached here, especially the colors for my Tennis GridRally App logo.

I will upload the Tennis GridRally logo which should go somewhere on the back cover design (small size maybe in the bottom corner).

This book is revolutionary to the standard way of teaching tennis, it is based on a decade of recording and gathering tennis data analytics and then we created on-court practice games to develop better decision making in players for the competitive edge.

My websites are www.elevatedrillzone.com and www.craftofsteadyrallies.com

```html
<!DOCTYPE html>
<html lang="en">
<head>
<meta charset="utf-8">
<title>The Craft of Steady Rallies – Cover Spread</title>
<link rel="stylesheet" href="https://fonts.googleapis.com/css2?family=Anton&family=Oswald:wght@300;400;500;700&display=swap">
<style>
  :root {
    --backdrop: #e9e9e9;
    --paper: #f6f6f4;
    --ink: #2a2a2a;
    --ink-soft: #3d3d3d;
    --blue: #2a62c6;
    --yellow: #f0b323;
    --white: #ffffff;
  }
  * { box-sizing: border-box; margin: 0; padding: 0; }
  html, body {
    width: 1200px; height: 1000px; overflow: hidden;
    background: var(--backdrop);
  }
  .spread {
    position: absolute; left: 49px; top: 100px;
    width: 1102px; height: 800px;
    display: flex;
    box-shadow: 0 10px 30px rgba(0,0,0,0.12);
  }
  .cover, .spine {
    position: relative; height: 100%;
    background: var(--paper);
    overflow: hidden;
  }
  .cover { width: 533px; }
  .spine { width: 36px; border-left: 1px solid #dcdcdc; border-right: 1px solid #dcdcdc; }

  .band {
    position: absolute; left: 0; right: 0; bottom: 0; height: 62px;
    background: var(--blue);
    display: flex; align-items: center; justify-content: center;
  }

  /* Title lockup */
  .title-lockup {
    font-family: "Anton", "Oswald", sans-serif;
    color: var(--ink);
    line-height: 1;
    display: inline-block;
  }
  .title-lockup .lead {
    font-family: "Oswald", sans-serif; font-weight: 700;
    font-size: 26px; display: block; padding-left: 70px;
    margin-bottom: -6px;
  }
  .title-lockup .main { font-size: 104px; letter-spacing: -1px; display: block; }
  .title-lockup .tail {
    font-family: "Oswald", sans-serif; font-weight: 700;
    font-size: 30px; display: block; text-align: right; margin-top: -4px;
  }

  /* Front cover */
  .front .title-lockup { position: absolute; left: 52px; top: 70px; }
  .brand-mark {
    position: absolute; left: 0; right: 0; top: 330px;
    display: flex; align-items: center; justify-content: center; gap: 14px;
    font-family: "Oswald", sans-serif; font-weight: 700;
    font-size: 34px; letter-spacing: 2px; color: var(--blue);
  }
  .brand-mark .dot {
    width: 26px; height: 26px; border-radius: 50%; background: var(--yellow);
  }
  .subtitle {
    position: absolute; left: 40px; right: 40px; top: 470px;
    text-align: center;
    font-family: "Oswald", sans-serif; font-weight: 400;
    font-size: 27px; line-height: 1.25; color: var(--ink-soft);
  }
  .author {
    font-family: "Oswald", sans-serif; font-weight: 700;
    letter-spacing: 3px; text-transform: uppercase;
  }
  .front .band .author { color: var(--white); font-size: 24px; }

  /* Spine */
  .spine-text {
    position: absolute; top: 30px; left: 50%;
    transform: translateX(-50%);
    writing-mode: vertical-rl;
    font-family: "Oswald", sans-serif; font-weight: 700;
    font-size: 17px; letter-spacing: 1.5px; color: var(--ink);
    white-space: nowrap;
  }
  .spine-text .sep { margin: 8px 0; }

  /* Back cover */
  .back .title-lockup { position: absolute; left: 110px; top: 52px; }
  .back .title-lockup .main { font-size: 80px; }
  .back .title-lockup .lead { font-size: 20px; padding-left: 54px; margin-bottom: -4px; }
  .back .title-lockup .tail { font-size: 24px; }
  .blurb {
    position: absolute; left: 50px; right: 50px; top: 218px;
    font-family: "Oswald", sans-serif; font-weight: 300;
    font-size: 13.2px; line-height: 1.42; color: var(--ink);
    text-align: left;
  }
  .blurb p { margin-bottom: 10px; }
  .blurb strong { font-weight: 700; }
  .app-name {
    position: absolute; right: 50px; bottom: 90px;
    display: flex; align-items: center; gap: 8px;
    font-family: "Oswald", sans-serif; font-weight: 500;
    font-size: 15px; color: var(--ink);
  }
  .app-name .circle { width: 14px; height: 14px; border-radius: 50%; background: var(--yellow); }
  .back .author-line {
    position: absolute; left: 50px; bottom: 84px;
    color: var(--ink); font-size: 24px;
  }
</style>
</head>
<body>
  <main class="spread">
    <section class="cover back" aria-label="Back cover">
      <h2 class="title-lockup">
        <span class="lead">The Craft of</span>
        <span class="main">Steady</span>
        <span class="tail">Rallies</span>
      </h2>
      <div class="blurb">
        <p>A practical guide on how to win more matches by becoming a more efficient and effective competitor.</p>
        <p>As a tennis player you have the ability to play better matches and win more of them. <strong>The Craft of Steady Rallies</strong> gives you a system to improve. We start with the individual game and the set itself. Our system examines your physical and mental progression, enabling you to upgrade your movement and performance from shot to shot and point to point.</p>
        <p>Our system seamlessly integrates the technical (physical) aspects with the tactical (mental/emotional) components, providing a comprehensive approach to elevate this performance. We aim to give you much more than how to hit great shots. Irrespective of your current skill level, we will provide you with a detailed strategic and tactical plan to enhance your performance, leading to improved results and increased success in your matches.</p>
        <p><strong>The Craft of Steady Rallies</strong> emphasizes the importance of shifting focus from oneself to the opponent, encouraging players to analyze and understand their adversaries. By bringing the opponent back to the forefront of their thinking, the player creates the best possible context in which to improve as a competitor.</p>
        <p>In this book, we present a groundbreaking approach to tennis data analytics that seamlessly integrates match performance with practice sessions, and vice versa.</p>
      </div>
      <p class="app-name"><span class="circle"></span>Tennis GridRally</p>
      <p class="author author-line">Corwin Haldane</p>
      <div class="band"></div>
    </section>

    <section class="spine" aria-label="Spine">
      <p class="spine-text">The Craft of Steady Rallies<span class="sep"> • </span>CORWIN HALDANE</p>
      <div class="band"></div>
    </section>

    <section class="cover front" aria-label="Front cover">
      <h1 class="title-lockup">
        <span class="lead">The Craft of</span>
        <span class="main">Steady</span>
        <span class="tail">Rallies</span>
      </h1>
      <div class="brand-mark"><span class="dot"></span>CRAFT OF STEADY</div>
      <p class="subtitle">Building a Tactical Margin<br>by Way of Opponent Insight</p>
      <div class="band"><p class="author">Corwin Haldane</p></div>
    </section>
  </main>
</body>
</html>
```